Steady Ground for Your Venture - book cover

A book cover (front) to be used on print book. Book will be 5 inches by 8 inches. Also need the cover image (as jpg) for promotional purposes. Include company logo on cover - I've included a couple of versions. Include my name as author: Dr. Lorinda Haskell

Title of book is:
Weatherizing Your Enterprise
(sub-title) by teaching thinking skills

this can be a sub-sub title, or a call out or "burst" standing alone -
A survival guide for 21st century business

If you'd like some inspiration, check out my web page: www.lessonmedic.net
The company colors are red, white and blue, but I think red might be too harsh - use with caution if you use it.
RGB values of the company are:
Blue: 0/66/105
Red: 190/30/45

Target Market(s)

Business / Professionals / Chief Executives of Companies with more than 1000 employees

Industry/Entity Type

Business

Font styles to use
Serif

Colors
0255a3
ffffff

Requirements
Must have
• The title should make them pause and say "I need to get this book if I want my company to survive another 20 years!"
Nice to have
• Some image that signifies the future and / or uncertainty. Should be abstract - not people, not technology (which could change and then make the book look old). If you'd like to make the design a wrap from front to back, that is fine. I am not sure what text will go on the back at this point, so I may have to come back to you in a few months for an update.

```html
<!DOCTYPE html>
<html lang="en">
<head>
<meta charset="utf-8">
<title>Weatherizing Your Enterprise — Book Cover</title>
<link rel="stylesheet" href="https://fonts.googleapis.com/css2?family=Cinzel:wght@400;500&family=EB+Garamond:ital,wght@0,500;0,600;1,400&display=swap">
<style>
  :root {
    --brand-blue: #0255a3;
    --brand-navy: #004269;
    --brand-red: #be1e2d;
    --paper: #ffffff;
    --haze: #eef0f3;
    --gold: #dcb878;
    --amber: #b99a63;
    --slate: #4a5668;
    --night: #16263a;
    --steel: #5d7fa3;
  }
  * { margin: 0; padding: 0; box-sizing: border-box; }
  html, body {
    width: 869px;
    height: 1200px;
    overflow: hidden;
    background: var(--paper);
  }
  .cover {
    position: relative;
    width: 869px;
    height: 1200px;
    background: linear-gradient(180deg, var(--paper) 0%, var(--haze) 55%, var(--paper) 100%);
    overflow: hidden;
  }
  .cover-art {
    position: absolute;
    left: 0;
    top: 0;
    width: 869px;
    height: 1018px;
  }
  .title-block {
    position: absolute;
    top: 78px;
    left: 0;
    width: 100%;
    text-align: center;
    color: var(--brand-blue);
    font-family: "Cinzel", "Times New Roman", serif;
  }
  .title-main {
    font-size: 86px;
    font-weight: 400;
    letter-spacing: 3px;
    line-height: 1;
  }
  .title-rest {
    margin-top: 22px;
    font-size: 34px;
    font-weight: 400;
    letter-spacing: 4px;
    line-height: 1;
    color: var(--brand-navy);
  }
  .subtitle {
    position: absolute;
    top: 462px;
    left: 66px;
    font-family: "EB Garamond", Georgia, serif;
    font-style: italic;
    font-size: 33px;
    line-height: 1;
    color: var(--brand-red);
    transform: rotate(-4deg);
    transform-origin: left center;
  }
  .author {
    position: absolute;
    top: 540px;
    left: 70px;
    font-family: "Cinzel", "Times New Roman", serif;
    font-size: 24px;
    letter-spacing: 2px;
    line-height: 1;
    color: var(--brand-navy);
  }
  .rule-red {
    position: absolute;
    left: 0;
    top: 1018px;
    width: 100%;
    height: 12px;
    background: var(--brand-red);
  }
  .publisher {
    position: absolute;
    top: 1056px;
    left: 0;
    width: 100%;
    text-align: center;
    color: var(--brand-navy);
    font-family: "EB Garamond", Georgia, serif;
    font-weight: 600;
  }
  .publisher-name {
    font-size: 84px;
    line-height: 1;
    letter-spacing: -1px;
  }
  .publisher-tagline {
    margin-top: 6px;
    padding-left: 250px;
    font-size: 25px;
    font-weight: 500;
    line-height: 1;
  }
</style>
</head>
<body>
  <main class="cover">
    <svg class="cover-art" viewBox="0 0 869 1018" role="img" aria-label="Double-exposure photograph of a person in silhouette holding a tablet beside a coffee cup, blended with a golden-lit city skyline">
      <defs>
        <linearGradient id="skyline-tone" x1="0" y1="0" x2="0" y2="1">
          <stop offset="0" stop-color="var(--gold)"/>
          <stop offset="0.3" stop-color="var(--amber)"/>
          <stop offset="0.6" stop-color="var(--slate)"/>
          <stop offset="1" stop-color="var(--night)"/>
        </linearGradient>
        <linearGradient id="table-tone" x1="0" y1="0" x2="0" y2="1">
          <stop offset="0" stop-color="var(--steel)" stop-opacity="0"/>
          <stop offset="0.35" stop-color="var(--steel)" stop-opacity="0.7"/>
          <stop offset="1" stop-color="var(--night)"/>
        </linearGradient>
        <radialGradient id="figure-fade" cx="0.72" cy="0.62" r="0.55">
          <stop offset="0.55" stop-color="#fff"/>
          <stop offset="1" stop-color="#fff" stop-opacity="0"/>
        </radialGradient>
        <mask id="figure-mask">
          <rect width="869" height="1018" fill="url(#figure-fade)"/>
        </mask>
      </defs>
      <rect x="360" y="280" width="509" height="738" fill="url(#skyline-tone)" mask="url(#figure-mask)"/>
      <rect x="0" y="820" width="869" height="198" fill="url(#table-tone)"/>
    </svg>

    <header class="title-block">
      <h1 class="title-main">WEATHERIZING</h1>
      <p class="title-rest">Your Enterprise</p>
    </header>

    <p class="subtitle">by teaching thinking skills</p>
    <p class="author">Dr. Lorinda Haskell</p>

    <div class="rule-red"></div>

    <footer class="publisher">
      <p class="publisher-name">Lesson Medic</p>
      <p class="publisher-tagline">sharper lessons for working teams</p>
    </footer>
  </main>
</body>
</html>
```